Values Statement poster template

We want to develop a poster template for our company policies and statements which promote our company values in our workplaces.
These documents are important in showing our clients, suppliers and employees who we are and what we stand for.
The graphic design will incorporate our company logo, and be bright, uplifting and inspiring, developing a graphic theme that we can utilise for other company documents. The design will graphically illustrate and support our values statement, with colour and modern design.
This values poster will be the first in a series of documents using the same theme.The format will be a4 and a3 portrait
We are an environmental service business specialising in rehabilitation and revegetation

Target Market(s)

Tier one clients in industry, Mining, Construction and agriculture

Font styles to use
Other font styles liked:
• calibri

Requirements
Must have
• Professional , high end feel, able to read clearly on a poster
Nice to have
• graphic design elements, symbols, etc which support the message, that can be carried through to various documents such as quality, environmental, safety policies
A bright theme which ties in with our logo colours.

```html
<!DOCTYPE html>
<html lang="en">
<head>
<meta charset="utf-8">
<title>Verdantis – Our Values</title>
<link rel="stylesheet" href="https://fonts.googleapis.com/css2?family=Crimson+Pro:ital,wght@0,700;1,400;1,600;1,700&display=swap">
<style>
  :root {
    --green: #3d8b40;
    --green-deep: #1f5e2a;
    --green-dark: #133d1c;
    --green-light: #6fb84a;
    --ink: #2f7a36;
    --paper: #ffffff;
    --gap: #f2f2f2;
  }
  * { margin: 0; padding: 0; box-sizing: border-box; }
  html, body { width: 1200px; height: 824px; overflow: hidden; background: var(--gap); }
  body { font-family: "Crimson Pro", Georgia, serif; color: var(--ink); }
  .canvas { position: relative; width: 1200px; height: 824px; }
  .page { position: absolute; top: 0; height: 824px; background: var(--paper); overflow: hidden; }
  .page--left { left: 0; width: 598px; }
  .page--right { left: 601px; width: 599px; }
  .swoosh { position: absolute; inset: 0; width: 100%; height: 100%; }
  .block { position: absolute; font-style: italic; }
  .title {
    position: absolute; left: 95px; top: 12px;
    font-family: "Crimson Pro", Georgia, serif; font-weight: 700; font-style: normal;
    font-size: 44px; letter-spacing: 1px; color: var(--green);
  }
  .leaf { position: absolute; top: 22px; width: 26px; height: 30px; border-radius: 0 60% 0 60%; background: var(--green-light); }
  .heading { font-weight: 700; font-size: 27px; line-height: 30px; color: var(--green); }
  .tagline { font-size: 23px; line-height: 28px; }
  .body { font-size: 16.5px; line-height: 20.7px; }
  .body-lg { font-size: 19.5px; line-height: 24px; }
  .indent { padding-left: 16px; }
  .logo-ring { position: absolute; left: 318px; top: 50px; width: 246px; height: 246px; }
  .brand { font-style: italic; font-weight: 600; color: var(--green); }
  .brand--ring { position: absolute; left: 352px; top: 152px; width: 180px; text-align: center; font-size: 30px; }
  .brand--small { position: absolute; left: 432px; top: 190px; font-size: 21px; }
  .placeholder { position: absolute; }
  .icon { position: absolute; }
</style>
</head>
<body>
<div class="canvas">

  <section class="page page--left">
    <svg class="swoosh" viewBox="0 0 598 824" aria-hidden="true">
      <defs>
        <linearGradient id="bandL" x1="0" y1="0" x2="1" y2="1">
          <stop offset="0" stop-color="#2f7d36"/>
          <stop offset="0.6" stop-color="#4a9b44"/>
          <stop offset="1" stop-color="#174a22"/>
        </linearGradient>
        <linearGradient id="cornerL" x1="0" y1="0" x2="1" y2="1">
          <stop offset="0" stop-color="#4ea447"/>
          <stop offset="1" stop-color="#2a7032"/>
        </linearGradient>
      </defs>
      <path d="M0,40 C40,120 10,260 40,380 C70,500 100,600 115,700 C122,760 128,800 130,824 L0,824 Z" fill="url(#bandL)"/>
      <path d="M0,470 C60,520 95,620 110,724 L116,824 L0,824 Z" fill="#133d1c" opacity="0.75"/>
      <path d="M440,0 L598,0 L598,480 C575,380 600,260 560,160 C530,90 480,40 440,0 Z" fill="url(#cornerL)"/>
      <path d="M500,0 L598,0 L598,90 C570,50 535,20 500,0 Z" fill="#1f5e2a"/>
    </svg>

    <span class="leaf" style="left:52px" role="img" aria-label="Leaf motif"></span>
    <h1 class="title">OUR VALUES</h1>
    <span class="leaf" style="left:360px" role="img" aria-label="Leaf motif"></span>

    <svg class="logo-ring" viewBox="0 0 246 246" aria-hidden="true">
      <circle cx="123" cy="123" r="118" fill="#ffffff"/>
      <path d="M123,5 A118,118 0 1 1 20,180 A108,108 0 1 0 123,15 Z" fill="#3d8b40"/>
      <path d="M20,180 A118,118 0 0 1 60,25 A110,110 0 0 0 30,170 Z" fill="#5aa84a"/>
    </svg>
    <div class="brand brand--ring">Verdantis</div>

    <p class="block tagline" style="left:79px; top:80px;">These are the things we<br>value most, they define<br>the way we do business</p>

    <h2 class="block heading" style="left:58px; top:192px;">We value our people<br>above everything else</h2>
    <p class="block body" style="left:56px; top:270px;">
      We demonstrate this by:<br>
      •&nbsp; Providing safe, positive, enjoyable workplaces where everyone feels<br>
      valued and respected<br>
      •&nbsp; Providing Careers, not Jobs, we grow together<br>
      •&nbsp; Encouraging inclusion, participation and collaboration<br>
      •&nbsp; Recognising and rewarding contribution and excellence<br>
      •&nbsp; Supporting our people through tough times
    </p>

    <h2 class="block heading" style="left:105px; top:455px;">We do good things for the planet</h2>
    <p class="block body-lg" style="left:193px; top:502px;">
      Our products are helping revegetate Australia,<br>
      which we are tremendously proud of.<br>
      We minimise our environmental impact in<br>
      everything we do.
    </p>

    <div class="placeholder" style="left:466px; top:593px; width:90px; height:90px; border-radius:50%; background:radial-gradient(circle at 40% 40%, #5aa84a, #2a7032);" role="img" aria-label="Globe with leaves icon"></div>

    <h2 class="block heading" style="left:155px; top:634px;">We set the standard</h2>
    <p class="block body-lg" style="left:152px; top:674px;">
      •&nbsp; We are uncompromising on quality<br>
      •&nbsp; We are the best at what we do, and we do what we<br>
      are best at<br>
      •&nbsp; We are always improving<br>
      •&nbsp; We are pioneering
    </p>

    <svg class="icon" style="left:471px; top:732px;" width="76" height="76" viewBox="0 0 76 76" role="img" aria-label="Quality tick badge">
      <circle cx="38" cy="38" r="36" fill="#2f7d36"/>
      <circle cx="38" cy="38" r="24" fill="none" stroke="#ffffff" stroke-width="4"/>
      <path d="M27,38 L35,46 L50,30" fill="none" stroke="#ffffff" stroke-width="5" stroke-linecap="round" stroke-linejoin="round"/>
    </svg>
  </section>

  <section class="page page--right">
    <svg class="swoosh" viewBox="0 0 599 824" aria-hidden="true">
      <defs>
        <linearGradient id="bandR" x1="0" y1="0" x2="1" y2="1">
          <stop offset="0" stop-color="#3f9140"/>
          <stop offset="1" stop-color="#174a22"/>
        </linearGradient>
      </defs>
      <path d="M0,0 L30,0 C10,150 30,330 70,500 C95,620 110,740 118,824 L0,824 Z" fill="url(#bandR)"/>
      <path d="M0,480 C50,540 80,650 95,824 L0,824 Z" fill="#133d1c" opacity="0.7"/>
      <path d="M440,0 L599,0 L599,300 C570,180 540,90 440,0 Z" fill="#4ea447"/>
      <path d="M520,0 L599,0 L599,110 C580,60 555,25 520,0 Z" fill="#1f5e2a"/>
    </svg>

    <h2 class="block heading" style="left:101px; top:14px;">Our workplaces are safe</h2>
    <p class="block body" style="left:61px; top:50px;">
      There is nothing more important to us than our people<br>
      going home healthy and safe every day. We won’t accept<br>
      anything less. We believe safety is a management choice. By<br>
      providing safe work systems, and education we achieve our<br>
      daily goal of Zero Harm. At Verdantis we;<br>
      •&nbsp; Take the time to make our work areas safe, whatever it<br>
      takes<br>
      •&nbsp; Don’t accept shortcuts<br>
      •&nbsp; Look out for each other<br>
      •&nbsp; Investigate our incidents and learn from them, we won’t<br>
      accept repeats<br>
      •&nbsp; Are constantly looking for ways to improve the safety of<br>
      our workplaces.<br>
      •&nbsp; Think safe, work safer, go home safe!
    </p>

    <div class="brand brand--small">Verdantis</div>

    <svg class="icon" style="left:493px; top:231px;" width="60" height="68" viewBox="0 0 60 68" role="img" aria-label="Safety shield icon">
      <path d="M30,2 L57,12 L57,34 C57,50 45,61 30,66 C15,61 3,50 3,34 L3,12 Z" fill="#3d9a40"/>
      <path d="M17,34 L27,44 L44,25" fill="none" stroke="#ffffff" stroke-width="6" stroke-linecap="round" stroke-linejoin="round"/>
    </svg>

    <h2 class="block heading" style="left:42px; top:348px;">We are proud of who we are</h2>
    <p class="block body" style="left:79px; top:384px;">
      Our reputation means the world to us. We:<br>
      •&nbsp; Treat everyone with respect and we expect it in return<br>
      •&nbsp; Follow the rules<br>
      •&nbsp; Do what we say we will do<br>
      •&nbsp; Own our mistakes and we fix them<br>
      •&nbsp; Are trustworthy and transparent
    </p>

    <svg class="icon" style="left:456px; top:444px;" width="80" height="76" viewBox="0 0 80 76" role="img" aria-label="Thumbs up icon">
      <rect x="2" y="36" width="18" height="38" rx="2" fill="#3d9a40"/>
      <circle cx="11" cy="64" r="2.5" fill="#ffffff"/>
      <path d="M24,36 L40,14 C42,6 46,2 50,4 C54,6 53,14 50,26 L72,26 C78,26 80,32 76,36 C80,40 78,46 74,47 C77,51 75,56 70,57 C72,62 69,67 64,67 L34,67 C28,67 24,64 24,60 Z" fill="#3d9a40"/>
    </svg>

    <h2 class="block heading" style="left:113px; top:517px;">We succeed together</h2>
    <p class="block body" style="left:153px; top:552px;">
      We believe in win-win relationships. When our business is<br>
      profitable everyone benefits, our owners, employees, clients<br>
      and the community. At Verdantis we:<br>
      •&nbsp; Work as a team, we get it done together<br>
      •&nbsp; We treat our suppliers and subcontractors like they are<br>
      part of the team.<br>
      •&nbsp; Are building on our success, and growing together<br>
      •&nbsp; Choose to work with employees, customers and suppliers<br>
      who fit our values
    </p>

    <h2 class="block heading" style="left:164px; top:746px;">We give back</h2>
    <p class="block body-lg" style="left:145px; top:776px;">
      We appreciate our success and we give back by sup-<br>
      porting our community, and those less fortunate.
    </p>
  </section>

</div>
</body>
</html>
```